BBQ Grill Tongs Logo and Packaging Design

Need fun exciting logo design and packaging for the best BBQ and Grilling tongs ever used.
Company Name is
Pruvel's Tongs
www.hearthclampco.com
Template layout for packaging is flat 5 x 8
We want the packaging to jump off the shelf in an eye catching design that uses vibrant colors and terminology such as..
NO more sore hands
Never Slips
Lifetime Guarantee
Best for Indoor and Outdoor BBQ and Cooking
Used by the BEST BBQ Grillmasters and Cooks
Reason: need some better designers
Target Market(s)
outdoor and indoor cooks, all ages people who purchase bbq supplies, cooking supplies and or bbq and grilling enthusists
Industry/Entity Type
Cooking
Requirements
Must have
- Bold Branding, bright colors
Nice to have
- http://www.tedmorlanz.com/
- http://www.lunadeverra.com/
- http://www.foxhollowcider.com/

```html
<!DOCTYPE html>
<html lang="en">
<head>
<meta charset="utf-8">
<title>Pruvel's Tongs – Packaging</title>
<link href="https://fonts.googleapis.com/css2?family=Ubuntu:wght@500;700&display=swap" rel="stylesheet">
<style>
  :root {
    --paper: #ffffff;
    --band-black: #0e0e0e;
    --band-grey: #3a3a3a;
    --flame-red: #f2473a;
    --flame-red-light: #f7614f;
    --flame-red-deep: #e0382b;
    --window-black: #1b1b1b;
    --steel-light: #8c8c8c;
    --steel-dark: #3c3c3c;
    --ink-white: #ffffff;
    --ink-yellow: #f5c518;
    --ink-dark: #2a1a1a;
    --pill-black: #161616;
  }
  * { margin: 0; padding: 0; box-sizing: border-box; }
  html, body { width: 900px; height: 1200px; overflow: hidden; background: var(--paper); }
  body { font-family: "Ubuntu", Arial, sans-serif; position: relative; }

  .package {
    position: absolute; left: 192px; top: 150px; width: 516px; height: 900px;
    overflow: hidden;
    background: var(--flame-red);
  }
  .flame-texture {
    position: absolute; inset: 0;
    background:
      radial-gradient(ellipse 60px 160px at 30px 300px, var(--flame-red-light) 0%, transparent 100%),
      radial-gradient(ellipse 60px 160px at 486px 420px, var(--flame-red-light) 0%, transparent 100%),
      radial-gradient(ellipse 60px 180px at 24px 620px, var(--flame-red-deep) 0%, transparent 100%),
      radial-gradient(ellipse 60px 180px at 490px 650px, var(--flame-red-deep) 0%, transparent 100%),
      radial-gradient(ellipse 220px 80px at 120px 740px, var(--flame-red-light) 0%, transparent 100%),
      radial-gradient(ellipse 220px 80px at 400px 860px, var(--flame-red-light) 0%, transparent 100%),
      linear-gradient(180deg, var(--flame-red) 0%, var(--flame-red-deep) 100%);
  }
  .header-band {
    position: absolute; left: 0; top: 0; width: 516px; height: 212px;
    background:
      radial-gradient(ellipse 200px 90px at 40% 45%, #4a4a4a 0%, transparent 100%),
      radial-gradient(ellipse 160px 70px at 70% 70%, #333 0%, transparent 100%),
      radial-gradient(ellipse at 50% 40%, var(--band-grey) 0%, var(--band-black) 80%);
    display: flex; align-items: center; justify-content: center;
  }
  .brand-name {
    color: var(--ink-white); font-weight: 700; font-size: 54px; letter-spacing: 2px;
    line-height: 1; text-transform: uppercase; margin-top: -8px;
  }
  .product-window {
    position: absolute; left: 56px; top: 212px; width: 404px; height: 478px;
    background:
      radial-gradient(ellipse 110px 230px at 50% 45%, var(--steel-dark) 0%, transparent 100%),
      radial-gradient(ellipse 40px 200px at 44% 40%, var(--steel-light) 0%, transparent 100%),
      radial-gradient(ellipse 40px 200px at 58% 40%, var(--steel-light) 0%, transparent 100%),
      var(--window-black);
  }
  .guarantee-badge {
    position: absolute; left: 300px; top: 550px; width: 200px; height: 180px;
  }
  .claims {
    position: absolute; left: 0; top: 728px; width: 516px; text-align: center;
    color: var(--ink-white); font-weight: 700; font-size: 23px; line-height: 29px;
  }
  .usage-pill {
    position: absolute; left: 66px; top: 800px; width: 384px; height: 52px;
    background: var(--pill-black); border-radius: 26px;
    color: var(--ink-white); font-weight: 500; font-size: 14px; line-height: 20px;
    text-align: center; padding-top: 6px;
  }
  .usage-pill .highlight { color: var(--ink-yellow); }
  .website {
    position: absolute; left: 0; top: 864px; width: 516px; text-align: center;
    color: var(--ink-dark); font-weight: 500; font-size: 16px;
  }
</style>
</head>
<body>
  <div class="package">
    <div class="flame-texture" role="img" aria-label="Red flame pattern background"></div>

    <header class="header-band">
      <h1 class="brand-name">Pruvel's Tongs</h1>
    </header>

    <div class="product-window" role="img" aria-label="Pair of stainless steel grill tongs shown through the package window"></div>

    <svg class="guarantee-badge" viewBox="0 0 200 180" aria-label="Lifetime Guarantee badge">
      <g transform="translate(104 94) rotate(-8)">
        <g fill="var(--flame-red)">
          <rect x="-74" y="-74" width="148" height="148"/>
          <rect x="-74" y="-74" width="148" height="148" transform="rotate(22.5)"/>
          <rect x="-74" y="-74" width="148" height="148" transform="rotate(45)"/>
          <rect x="-74" y="-74" width="148" height="148" transform="rotate(67.5)"/>
        </g>
        <g fill="var(--pill-black)">
          <rect x="-62" y="-62" width="124" height="124"/>
          <rect x="-62" y="-62" width="124" height="124" transform="rotate(22.5)"/>
          <rect x="-62" y="-62" width="124" height="124" transform="rotate(45)"/>
          <rect x="-62" y="-62" width="124" height="124" transform="rotate(67.5)"/>
        </g>
        <g fill="var(--ink-yellow)" font-family="Ubuntu, Arial, sans-serif" font-weight="700" font-size="22" text-anchor="middle">
          <text x="0" y="-4">Lifetime</text>
          <text x="0" y="23">Guarantee</text>
        </g>
      </g>
    </svg>

    <div class="claims">
      <p>NO more sore hands</p>
      <p>Never Slips</p>
    </div>

    <div class="usage-pill">
      <p>Best for Indoor and Outdoor BBQ and Cooking</p>
      <p>Used by the <span class="highlight">BEST BBQ</span> Grillmasters and Cooks</p>
    </div>

    <p class="website">www.hearthclampco.com</p>
  </div>
</body>
</html>
```